Rug Cleaning Web Design Project

We need a web design for our cleaning company. We currently have a web page but are not happy with its design. We currently offer fine rug cleaning,upholstery cleaning, and residential and commercial carpet cleanning. We also offer water damage restoration. For our rug cleaning services we offer : Enzyme treatments for pet contamination and odor removal, application of stain protection that is designed for the fine textiles used in rug construction, application of treatments designed to prevent moth damage and pads designed to be used under rugs.Our current web site is harborfreshcare.example. We are intrested in a design with similar information to the web page of Velmora Rug Cleaners INC. We would like to use the colors that are present in our logo that will be uploaded with this description. We would also like this new page to be linked to our other address loomrinsepro.example. We would like the deign to be visually attractive but not "too busy".
Updates

Please include pictures of rugs, or people washing rugs if possible. We do not offer maid type cleaning services. We would not be interested in designs including pictures depicting that type service. Thanks for your hard work on this project.

Dana Whitlow

Industry/Entity Type

Residential

Requirements
Must have
• This page must be viewable on smart phones and tablets.

```html
<!DOCTYPE html>
<html lang="en">
<head>
<meta charset="utf-8">
<meta name="viewport" content="width=device-width, initial-scale=1">
<title>LoomRinsePro — Fine Rug Washing</title>
<link rel="stylesheet" href="https://fonts.googleapis.com/css2?family=Gelasio&family=Open+Sans:wght@400;600&family=Arimo&display=swap">
<style>
  :root {
    --white: #ffffff;
    --ink: #222222;
    --nav-ink: #2b2b2b;
    --brand-blue: #1f7fc4;
    --band-dark: #3a3a3a;
    --band-mid: #6a6a6a;
    --panel-dark: #141414;
    --bar-light: #d6d6d6;
    --hero-text: #f2f2f2;
    --body-text: #333333;
    --photo-warm: #c9b9a2;
    --photo-cool: #56606c;
  }
  * { box-sizing: border-box; margin: 0; padding: 0; }
  html, body { width: 1200px; height: 660px; overflow: hidden; background: var(--white); }
  body { position: relative; font-family: "Arimo", Arial, sans-serif; color: var(--ink); }

  .site-header { position: absolute; top: 0; left: 0; width: 1200px; height: 70px; background: var(--white); z-index: 2; box-shadow: 0 1px 3px rgba(0,0,0,.25); }
  .brand { position: absolute; left: 203px; top: 16px; display: flex; align-items: center; gap: 10px; }
  .brand-dot { width: 30px; height: 30px; border-radius: 50%; background: var(--brand-blue); }
  .brand-name { font-family: "Open Sans", sans-serif; font-weight: 600; font-size: 25px; color: var(--ink); letter-spacing: -0.5px; }
  .main-nav { position: absolute; right: 195px; top: 33px; display: flex; gap: 30px; }
  .main-nav a { font-family: "Open Sans", sans-serif; font-size: 14.5px; color: var(--nav-ink); text-decoration: none; }

  .hero-band { position: absolute; top: 70px; left: 0; width: 1200px; height: 450px;
    background: radial-gradient(ellipse at 50% 40%, var(--band-mid) 0%, var(--band-dark) 75%); }
  .hero { position: absolute; left: 194px; top: 34px; width: 815px; height: 374px; border: 1px solid #8a96a6;
    box-shadow: 0 22px 18px -12px rgba(0,0,0,.7); overflow: hidden; }
  .hero-services { position: absolute; left: 0; top: 0; width: 324px; height: 100%;
    background: linear-gradient(180deg, #1b1b1b, var(--panel-dark) 60%, #242424); }
  .service { position: absolute; left: 0; width: 324px; text-align: center; font-family: "Gelasio", Georgia, serif;
    font-size: 27px; line-height: 35px; color: var(--hero-text); white-space: nowrap; }
  .service-rug { top: 75px; }
  .service-water { top: 168px; font-size: 24px; letter-spacing: -0.2px; }
  .service-carpet { top: 257px; }
  .service-bar { position: absolute; left: 0; width: 324px; height: 9px; background: var(--bar-light); }
  .bar-one { top: 134px; }
  .bar-two { top: 229px; }
  .hero-photo { position: absolute; left: 324px; top: 0; width: 491px; height: 100%;
    background: linear-gradient(100deg, var(--photo-cool) 0%, #8c8478 25%, var(--photo-warm) 55%, #a7a4a2 80%, #5f6670 100%); }

  .content-band { position: absolute; top: 520px; left: 0; width: 1200px; height: 140px;
    background: linear-gradient(180deg, #ececec 0px, var(--white) 30px); }
  .intro { position: absolute; top: 36px; width: 250px; font-size: 10.2px; line-height: 17px; color: var(--body-text); }
  .intro-left { left: 194px; }
  .intro-middle { left: 476px; }
  .product-photo { position: absolute; left: 758px; top: 33px; width: 170px; height: 120px;
    background: linear-gradient(160deg, #f7f8f4 0%, #eef1e6 45%, #b6d64a 70%, #8fbf2a 100%); }
</style>
</head>
<body>
  <header class="site-header">
    <div class="brand">
      <span class="brand-dot"></span>
      <span class="brand-name">LoomRinsePro</span>
    </div>
    <nav class="main-nav">
      <a href="#">About Us</a>
      <a href="#">Rug Washing</a>
      <a href="#">Water Damage</a>
      <a href="#">Carpet Cleaning</a>
      <a href="#">Contact us</a>
    </nav>
  </header>

  <section class="hero-band">
    <div class="hero">
      <div class="hero-services">
        <p class="service service-rug">Fine Rug Washing</p>
        <span class="service-bar bar-one"></span>
        <p class="service service-water">Water Damage Restoration</p>
        <span class="service-bar bar-two"></span>
        <p class="service service-carpet">Carpet &amp; Upholstery<br>Cleaning</p>
      </div>
      <div class="hero-photo" role="img" aria-label="Photo of a cleaning technician mopping a marble hallway floor"></div>
    </div>
  </section>

  <section class="content-band">
    <p class="intro intro-left">Lorem ipsum dolor sit amet, consectetuer adipiscing elit, sed diam nonummy nibh euismod tincidunt ut laoreet dolore magna aliquam erat volutpat. Ut wisi enim ad minim veniam, quis nostrud exerci tation ullamcorper suscipit lobortis nisl ut aliquip ex ea commodo consequat. Duis autem vel eum iriure</p>
    <p class="intro intro-middle">Lorem ipsum dolor sit amet, consectetuer adipiscing elit, sed diam nonummy nibh euismod tincidunt ut laoreet dolore magna aliquam erat volutpat. Ut wisi enim ad minim veniam, quis nostrud exerci tation ullamcorper suscipit lobortis nisl ut aliquip ex ea commodo consequat. Duis autem vel eum iriure</p>
    <div class="product-photo" role="img" aria-label="Photo of a green cleaning caddy with supplies"></div>
  </section>
</body>
</html>
```